we do all sorts of cleaning however bookings are limited!
why not chose the right cleaners for you!
pressure cleaning, window cleaning, office, end of lease clean, accommodation, industrial and commercial cleaning and house cleaning

Logo Text

Bright Nest Cleaning Service

```html
<!DOCTYPE html>
<html lang="en">
<head>
<meta charset="utf-8">
<title>Bright Nest Cleaning Service – Business Card</title>
<link rel="stylesheet" href="https://fonts.googleapis.com/css2?family=Poppins:wght@400;600;700&family=Kaushan+Script&display=swap">
<style>
  :root {
    --blue: #29a8e0;
    --green: #8cc63f;
    --ink: #000000;
    --paper: #ffffff;
    --text: #2b2b2b;
    --backdrop: #e9e7e4;
  }
  * { margin: 0; padding: 0; box-sizing: border-box; }
  html, body { width: 1189px; height: 1200px; overflow: hidden; background: var(--backdrop); }
  body { position: relative; font-family: "Poppins", sans-serif; }

  .card {
    position: absolute;
    left: 169px;
    width: 851px;
    height: 484px;
    border-radius: 30px;
    overflow: hidden;
    box-shadow: 0 8px 22px rgba(0,0,0,0.18);
  }
  .card--front { top: 93px; background: var(--ink); }
  .card--back { top: 620px; background: var(--paper); }

  .brand-name {
    position: absolute;
    color: var(--blue);
    font-weight: 700;
    line-height: 1;
    text-align: center;
  }
  .card--front .brand-name { left: 0; right: 0; top: 186px; font-size: 66px; }
  .card--front .brand-name small { display: block; font-size: 25px; margin-top: 10px; letter-spacing: 1px; }
  .card--back .brand-name { left: 43px; width: 340px; top: 190px; font-size: 46px; }
  .card--back .brand-name small { display: block; font-size: 17px; margin-top: 8px; letter-spacing: 0.5px; }

  .front-web {
    position: absolute; left: 0; right: 0; top: 395px;
    text-align: center; color: var(--green);
    font-size: 19px; letter-spacing: 4px; font-weight: 400;
  }

  .divider {
    position: absolute; left: 406px; top: 131px;
    width: 1.5px; height: 184px; background: var(--blue);
  }

  .contact { position: absolute; left: 472px; top: 100px; color: var(--text); }
  .contact__name { font-family: "Kaushan Script", cursive; font-size: 38px; line-height: 1.1; }
  .contact__name .first { color: var(--blue); }
  .contact__name .last { color: var(--green); }
  .contact__role { font-size: 19px; line-height: 1; margin-top: -2px; }
  .contact__address { font-size: 19px; line-height: 28px; margin-top: 27px; }
  .contact__list { list-style: none; margin-top: 12px; font-size: 19px; }
  .contact__list li { display: flex; align-items: center; gap: 12px; height: 28px; }
  .contact__list svg { width: 22px; height: 22px; flex: none; }

  .wave { position: absolute; left: 0; bottom: 0; width: 851px; height: 130px; }

  .back-web {
    position: absolute; right: 34px; bottom: 28px;
    color: var(--paper); font-size: 19px;
  }
  .back-web span { color: var(--blue); }
</style>
</head>
<body>
  <section class="card card--front">
    <div class="brand-name">Bright Nest<small>CLEANING SERVICE</small></div>
    <p class="front-web">www.brightnestclean.com</p>
  </section>

  <section class="card card--back">
    <div class="brand-name">Bright Nest<small>CLEANING SERVICE</small></div>
    <div class="divider"></div>

    <div class="contact">
      <p class="contact__name"><span class="first">Liam</span> <span class="last">Carter</span></p>
      <p class="contact__role">Managing Partner</p>
      <p class="contact__address">PO BOX 456 Harbour Road<br>4th street Geelong</p>
      <ul class="contact__list">
        <li>
          <svg viewBox="0 0 22 22" aria-hidden="true">
            <circle cx="11" cy="11" r="11" fill="var(--blue)"/>
            <rect x="7" y="5" width="8" height="12" rx="1.5" fill="none" stroke="#fff" stroke-width="1.8"/>
            <circle cx="11" cy="14.6" r="0.9" fill="#fff"/>
          </svg>
          555-014-2290
        </li>
        <li>
          <svg viewBox="0 0 22 22" aria-hidden="true">
            <circle cx="11" cy="11" r="11" fill="var(--blue)"/>
            <rect x="5.5" y="7" width="11" height="8" rx="1" fill="none" stroke="#fff" stroke-width="1.6"/>
            <path d="M5.8 7.5 L11 11.8 L16.2 7.5" fill="none" stroke="#fff" stroke-width="1.6"/>
          </svg>
          hello@brightnestmail.com
        </li>
      </ul>
    </div>

    <svg class="wave" viewBox="0 0 851 130" preserveAspectRatio="none" aria-hidden="true">
      <path d="M0 22 C 160 90, 300 110, 470 92 C 620 74, 740 10, 851 12 L851 130 L0 130 Z" fill="var(--ink)"/>
      <path d="M0 10 C 150 80, 300 98, 470 80 C 620 62, 740 0, 838 2 C 740 8, 620 70, 470 90 C 300 108, 150 90, 0 18 Z" fill="var(--blue)"/>
    </svg>
    <p class="back-web">www.<span>brightnestclean</span>.com</p>
  </section>
</body>
</html>
```